Need a stunning home page for Car rental company

For a client, I need a slick and sumber home page design. It is a small, local car rental company, with a handful of cars available for rent.
Selling points: affordable lease, availability, always clean cars
The design should be:
- flat and modern
- no, or very few animations/sliders
- CTA: booking form for renting a car.
- 3 featured cars with images and facts (see website) with button to read more about the car.
- fullscreen background video can be an option
- main colour: #efba01
The site is under construction here:
http://tormesbil.ulvenkor.no/
Delivery requirements:
I need a layered & well organised PSD file delivered.

```html
<!DOCTYPE html>
<html lang="no">
<head>
<meta charset="utf-8">
<title>Tormes Bilutleie</title>
<link href="https://fonts.googleapis.com/css2?family=Roboto:wght@400;500;700&display=swap" rel="stylesheet">
<style>
:root{
  --brand:#efba01;
  --ink:#222;
  --text:#3a3a3a;
  --muted:#777;
  --line:#d6d6d6;
  --card:#f3f3f4;
  --footer:#8a8a8a;
  --green:#3f8a12;
  --green-dark:#2a6a08;
}
*{box-sizing:border-box;margin:0;padding:0}
html,body{width:1048px;height:1200px;overflow:hidden}
body{font-family:'Roboto',sans-serif;color:var(--text);background:#fff;position:relative}
.abs{position:absolute}

/* header */
.site-header{position:absolute;left:0;top:0;width:1048px;height:73px;background:linear-gradient(#fff,#f3f3f3)}
.brand{position:absolute;left:134px;top:19px;display:flex;align-items:center;gap:8px;font-weight:700;font-size:27px;letter-spacing:1px;color:#5a5a5a}
.brand-dot{width:14px;height:14px;border-radius:50%;background:var(--brand)}
.search{position:absolute;left:734px;top:18px;width:181px;height:29px;border:1px solid #c9c9c9;background:#fff;display:flex}
.search span{flex:1;font-size:9px;color:#555;padding:9px 0 0 8px}
.search b{width:28px;background:#8d8d8d;display:flex;align-items:center;justify-content:center}

/* nav */
.main-nav{position:absolute;left:0;top:73px;width:1048px;height:40px;background:var(--brand)}
.main-nav ul{list-style:none;position:absolute;left:126px;top:0;display:flex;height:40px;align-items:center}
.main-nav li{font-size:10.5px;font-weight:500;color:#1a1a1a;padding:0 24px;height:20px;line-height:20px;border-left:1px solid rgba(255,255,255,.7)}
.main-nav li:first-child{border-left:none;padding-left:17px}
.flags{position:absolute;left:876px;top:13px;display:flex;gap:8px}

/* hero */
.hero{position:absolute;left:0;top:113px;width:1048px;height:443px;background:linear-gradient(100deg,#3a2a1c 0%,#8a5a2c 35%,#d29a55 55%,#7a5234 78%,#2c2018 100%)}
.play{position:absolute;left:735px;top:156px}
.dots{position:absolute;left:495px;top:523px;display:flex;gap:4px}
.dots i{width:10px;height:10px;border-radius:50%;background:#fff;display:block}
.dots i.on{background:#333;border:3px solid #fff}

.booking{position:absolute;left:132px;top:113px;width:379px;height:304px;background:#fff;border-radius:0 0 4px 4px;box-shadow:0 3px 10px rgba(0,0,0,.35)}
.booking h2{position:absolute;left:40px;top:23px;font-weight:400;font-size:21px;color:var(--brand)}
.booking .ico{position:absolute;left:16px;top:28px}
.lbl{position:absolute;font-size:11.5px;color:#222}
.field{position:absolute;height:27px;border:1px solid #c8c8c8;background:#fff;font-size:9.5px;color:#666;padding:8px 0 0 6px}
.field .caret{position:absolute;right:6px;top:11px;border:4px solid transparent;border-top:5px solid #222;border-bottom:none}
.field .cal{position:absolute;right:5px;top:6px}
.book-btn{position:absolute;left:260px;top:257px;width:105px;height:29px;border-radius:4px;background:linear-gradient(var(--green),var(--green-dark));color:#fff;font-size:11.5px;font-weight:500;text-align:center;line-height:29px}

.call{position:absolute;left:215px;top:443px;width:193px;height:53px;background:var(--brand);border-radius:3px}
.call .divider{position:absolute;left:52px;top:10px;width:1px;height:33px;background:#6b5200}
.call small{position:absolute;left:64px;top:10px;font-size:11px;font-weight:700;color:#111}
.call strong{position:absolute;left:64px;top:20px;font-size:24px;font-weight:400;color:#111}

/* welcome */
.welcome{position:absolute;left:0;top:573px;width:1048px;text-align:center}
.welcome h1{font-size:16px;font-weight:700;color:var(--brand);letter-spacing:.3px}
.welcome p{font-size:10px;line-height:16px;color:#333;margin-top:7px}

/* cars */
.car{position:absolute;top:654px;width:252px;height:425px;background:var(--card)}
.car-photo{height:167px}
.car h3{position:absolute;left:13px;top:176px;font-size:14.5px;font-weight:700;color:var(--brand)}
.price{position:absolute;left:14px;top:197px;width:218px;display:flex;justify-content:space-between;font-size:10px}
.price b{font-size:11.5px;margin-right:13px}
.specs{position:absolute;left:14px;top:220px;width:226px;list-style:none;font-size:10px}
.specs li{height:24.2px;display:flex;align-items:center;border-bottom:1px solid var(--line)}
.specs li:last-child{border-bottom:none}
.specs span{width:176px}
.specs b{font-size:10px}
.more{position:absolute;left:85px;top:410px;width:82px;height:25px;border-radius:4px;background:linear-gradient(#333,#000);color:#fff;font-size:9.5px;font-weight:700;text-align:center;line-height:25px}

/* footer */
.site-footer{position:absolute;left:0;top:1115px;width:1048px;height:85px;background:var(--footer);color:#fff}
.follow{position:absolute;left:133px;top:24px;font-size:9px;font-weight:500}
.social{position:absolute;left:133px;top:40px;display:flex;gap:6px}
.social i{width:20px;height:20px;border-radius:50%;display:block;border:1px solid rgba(255,255,255,.6)}
.foot-nav{position:absolute;right:131px;top:24px;font-size:9px;font-weight:500;text-align:right;line-height:16px}
</style>
</head>
<body>

<header class="site-header">
  <div class="brand"><span class="brand-dot"></span>TORMESBILUTLEIE</div>
  <div class="search"><span>SEARCH</span><b><svg width="14" height="14" viewBox="0 0 14 14"><circle cx="6" cy="6" r="4.5" fill="none" stroke="#fff" stroke-width="1.5"/><line x1="9.3" y1="9.3" x2="13" y2="13" stroke="#fff" stroke-width="1.6"/></svg></b></div>
</header>

<nav class="main-nav">
  <ul>
    <li>HOME</li><li>ABOUT US</li><li>CAR LEASING</li><li>OUR FLEET</li><li>SERVICES</li><li>BLOG</li><li>CONTACT US</li>
  </ul>
  <div class="flags">
    <svg width="15" height="10" viewBox="0 0 15 10"><rect width="15" height="10" fill="#1f3a8a"/><rect x="6" width="3" height="10" fill="#fff"/><rect y="3.5" width="15" height="3" fill="#fff"/><rect x="6.7" width="1.6" height="10" fill="#c8102e"/><rect y="4.2" width="15" height="1.6" fill="#c8102e"/></svg>
    <svg width="15" height="10" viewBox="0 0 15 10"><rect width="15" height="10" fill="#c8102e"/><rect x="4" width="3" height="10" fill="#fff"/><rect y="3.5" width="15" height="3" fill="#fff"/><rect x="4.8" width="1.4" height="10" fill="#1f3a8a"/><rect y="4.3" width="15" height="1.4" fill="#1f3a8a"/></svg>
  </div>
</nav>

<section class="hero" role="img" aria-label="Photo of a bronze SUV driving on a highway past a city skyline at sunset">
  <svg class="play" width="70" height="70" viewBox="0 0 70 70"><circle cx="35" cy="35" r="31" fill="none" stroke="#fff" stroke-width="6"/><path d="M28 22 L50 35 L28 48 Z" fill="#fff"/></svg>
  <div class="dots"><i></i><i class="on"></i><i></i><i></i></div>
</section>

<form class="booking">
  <svg class="ico" width="16" height="16" viewBox="0 0 16 16"><circle cx="6.5" cy="6.5" r="5" fill="none" stroke="#999" stroke-width="1.4"/><line x1="10.2" y1="10.2" x2="15" y2="15" stroke="#999" stroke-width="1.6"/></svg>
  <h2>Search for a car rental</h2>
  <div class="lbl" style="left:16px;top:63px">Location</div>
  <div class="field" style="left:16px;top:79px;width:347px">Enter City or Zipcode</div>

  <div class="lbl" style="left:16px;top:124px">Pickup Date</div>
  <div class="field" style="left:16px;top:140px;width:96px">dd/mm/yy<svg class="cal" width="13" height="13" viewBox="0 0 13 13"><rect x=".5" y="1.5" width="12" height="11" fill="none" stroke="#555"/><path d="M3 5h7M3 7.5h7M3 10h7M5 4v8M8 4v8" stroke="#555" stroke-width=".8"/></svg></div>
  <div class="field" style="left:115px;top:140px;width:69px">10:00 PM<span class="caret"></span></div>

  <div class="lbl" style="left:195px;top:124px">Drop off Date</div>
  <div class="field" style="left:195px;top:140px;width:96px">dd/mm/yy<svg class="cal" width="13" height="13" viewBox="0 0 13 13"><rect x=".5" y="1.5" width="12" height="11" fill="none" stroke="#555"/><path d="M3 5h7M3 7.5h7M3 10h7M5 4v8M8 4v8" stroke="#555" stroke-width=".8"/></svg></div>
  <div class="field" style="left:294px;top:140px;width:69px">10:00 PM<span class="caret"></span></div>

  <div class="lbl" style="left:16px;top:181px">Age &amp; Residence</div>
  <div class="field" style="left:16px;top:201px;width:53px">25+<span class="caret"></span></div>

  <div class="lbl" style="left:196px;top:181px">Car&nbsp; Type</div>
  <div class="field" style="left:196px;top:201px;width:118px">&nbsp;Choose car Type<span class="caret"></span></div>

  <div class="book-btn">BOOK NOW</div>
</form>

<div class="call">
  <svg class="abs" style="left:17px;top:15px" width="26" height="22" viewBox="0 0 26 22"><path d="M2 8 C2 2 24 2 24 8 L24 10 L18 10 L18 7 L8 7 L8 10 L2 10 Z" fill="#111"/><path d="M5 11 L9 8 L17 8 L21 11 L22 20 L4 20 Z" fill="#111"/><circle cx="13" cy="14" r="3" fill="#efba01"/></svg>
  <span class="divider"></span>
  <small>CALL US</small>
  <strong>91234567</strong>
</div>

<section class="welcome">
  <h1>WELCOME TO OUR SITE</h1>
  <p>Tormes bilutleie er en bilpark på Vikstrand, og leier ut varebiler og personbiler til deg som trenger en ekstrabil til flytting, ferie, bytur eller hva det måtte være.<br>Vi er uslåelige på service, og mest sannsynlig også på pris. Og du kan stole på at bilen du får fra oss er både ren og pen!</p>
</section>

<article class="car" style="left:132px">
  <div class="car-photo" role="img" aria-label="Photo of a white van parked on gravel" style="background:linear-gradient(#cfd8e2 0%,#eef0f2 40%,#bdbdbd 75%,#8d8a84 100%)"></div>
  <h3>Varebilen</h3>
  <div class="price"><span>Pris per døgn</span><b>kr 600</b></div>
  <ul class="specs">
    <li><span>Biltype</span><b>Varebil</b></li>
    <li><span>VarebilMaks. pers.</span><b>2</b></li>
    <li><span>Ant. dører</span><b>5</b></li>
    <li><span>Min. sjåføralder</span><b>21</b></li>
    <li><span>Girtype</span><b>Manuell</b></li>
    <li><span>Klimaanlegg?</span><b>Ja</b></li>
    <li><span>Ubegrenset km?</span><b>Nei</b></li>
  </ul>
  <div class="more">READ MORE</div>
</article>

<article class="car" style="left:398px">
  <div class="car-photo" role="img" aria-label="Photo of a white luxury coupe parked by a gate" style="background:linear-gradient(#3b3b3b 0%,#6a6a66 35%,#e2e4e0 60%,#8a8a88 100%)"></div>
  <h3>Vikstrand</h3>
  <div class="price"><span>Pris per døgn</span><b>kr 600</b></div>
  <ul class="specs">
    <li><span>Biltype</span><b>Varebil</b></li>
    <li><span>VarebilMaks. pers.</span><b>2</b></li>
    <li><span>Ant. dører</span><b>5</b></li>
    <li><span>Min. sjåføralder</span><b>21</b></li>
    <li><span>Girtype</span><b>Manuell</b></li>
    <li><span>Klimaanlegg?</span><b>Ja</b></li>
    <li><span>Ubegrenset km?</span><b>Nei</b></li>
  </ul>
  <div class="more">READ MORE</div>
</article>

<article class="car" style="left:663px">
  <div class="car-photo" role="img" aria-label="Photo of a grey minivan by the sea" style="background:linear-gradient(#5a8fd0 0%,#9cc4e8 30%,#6d6c74 60%,#9a9aa0 100%)"></div>
  <h3>Bilutleie</h3>
  <div class="price"><span>Pris per døgn</span><b>kr 600</b></div>
  <ul class="specs">
    <li><span>Biltype</span><b>Varebil</b></li>
    <li><span>VarebilMaks. pers.</span><b>2</b></li>
    <li><span>Ant. dører</span><b>5</b></li>
    <li><span>Min. sjåføralder</span><b>21</b></li>
    <li><span>Girtype</span><b>Manuell</b></li>
    <li><span>Klimaanlegg?</span><b>Ja</b></li>
    <li><span>Ubegrenset km?</span><b>Nei</b></li>
  </ul>
  <div class="more">READ MORE</div>
</article>

<footer class="site-footer">
  <div class="follow">FOLLOW US ON</div>
  <div class="social"><i style="background:#2f5fa8"></i><i style="background:#3ea6e0"></i><i style="background:#f07a20"></i></div>
  <div class="foot-nav">HOME &nbsp;|&nbsp; ABOUT US &nbsp;|&nbsp; CAR LEASING &nbsp;|&nbsp; OUR FLEET &nbsp;|&nbsp; SERVICES &nbsp;|&nbsp; CONTACT US<br>COPYRIGHTS @ 2014 ALL RIGHTS RESERVED</div>
</footer>

</body>
</html>
```